Quirky Coffee Shop Loyalty Card

We need a new loyalty card in business card size format for our independent coffee shop. We are a quirky, ethically focussed, high quality coffee establishment with a focus on cutting edge products like siphon coffee and flamed latte brules. Projecting an image of high quality, innovation, ethical and eco-friendly with a quirky and unique feel. We would like a green background appearance, echoing or complementing the green in our logo (uploaded). Our coffee is organic and ethically sourced, we would like to communicate this - it doesn't need to be done in obvious way, open to creative suggestions. Earthy and straightforward in approach is important to us. We use cups made from 100% repurposed coffee husk, called Brindle (https://brindlecups.example/). One idea we had would be to have this cup image on the card with arrows pointing in from words like "Organic", "Made from coffee husks", "Ethical" etc... but in a less cliche'd way than this sounds!Please note that although this is a business card size, we need a loyalty card not a business card. On the back, we need to convey that the customer buys 8 coffees and gets the ninth free. We also need our social media links, email and address:
FB: @pebblekettlemossford
Insta: Pebblekettle
Email: mossford@pebblekettle.example
Address: No.4 Quill Row, ZX40 9KT
Phone: 01999 462057

Target Market(s)

All shop customers

Industry/Entity Type

Coffee Shop

Contact Information for Business Card

FB: @pebblekettlemossford
Insta: Pebblekettle
Phone: 01999 462057

Colors

Designer to choose colors to be used in the design.

Requirements
Must have
• Quirky, ethical, organic feel
Should not have
• Well-used or obvious coffee shop imagery

```html
<!DOCTYPE html>
<html lang="en">
<head>
<meta charset="utf-8">
<title>Pebble Kettle Loyalty Card</title>
<link rel="stylesheet" href="https://fonts.googleapis.com/css2?family=Montserrat+Alternates:wght@600&family=Questrial&display=swap">
<style>
  :root {
    --backdrop: #c4c4c4;
    --leaf: #6db52b;
    --leaf-dark: #4f8f1a;
    --roast: #8b3c12;
    --ink: #231f20;
    --cream: #ffffff;
  }
  html, body {
    margin: 0;
    width: 1200px;
    height: 1200px;
    overflow: hidden;
    background: var(--backdrop);
  }
  .sheet {
    position: relative;
    width: 1200px;
    height: 1200px;
  }
  .card {
    position: absolute;
    left: 140px;
    width: 920px;
    height: 526px;
    box-shadow: 6px 8px 14px rgba(0,0,0,0.35);
  }
  .card--front { top: 46px; }
  .card--back { top: 628px; }
  .card svg { display: block; }
  .headline {
    font-family: "Montserrat Alternates", sans-serif;
    font-weight: 600;
    font-size: 46px;
    letter-spacing: 0.12em;
  }
  .headline--light { fill: var(--cream); }
  .headline--roast { fill: var(--roast); }
  .contact {
    font-family: "Questrial", sans-serif;
    font-size: 17px;
    fill: var(--cream);
  }
  .brand-name {
    font-family: "Questrial", sans-serif;
    font-size: 22px;
    fill: var(--leaf-dark);
  }
  .stamp-number {
    font-family: "Questrial", sans-serif;
    font-size: 14px;
    font-weight: 700;
  }
  .free-label {
    font-family: "Questrial", sans-serif;
    font-size: 25px;
    fill: var(--roast);
  }
  .offer-title {
    font-family: "Questrial", sans-serif;
    font-size: 38px;
    fill: var(--leaf);
  }
  .offer-line {
    font-family: "Questrial", sans-serif;
    font-size: 28px;
    fill: var(--cream);
  }
</style>
</head>
<body>
<main class="sheet">

  <!-- Front -->
  <section class="card card--front">
    <svg width="920" height="526" viewBox="0 0 920 526">
      <defs>
        <linearGradient id="brew-photo" x1="0" y1="0" x2="1" y2="1">
          <stop offset="0" stop-color="#6b4a34"/>
          <stop offset="0.5" stop-color="#a4683a"/>
          <stop offset="1" stop-color="#4a2c1a"/>
        </linearGradient>
        <linearGradient id="bean-photo" x1="0" y1="0" x2="0" y2="1">
          <stop offset="0" stop-color="#5a3520"/>
          <stop offset="1" stop-color="#2a160c"/>
        </linearGradient>
      </defs>
      <rect class="card-base" width="920" height="526" fill="var(--ink)"/>
      <polygon role="img" aria-label="Photo of a copper coffee pot with frothed coffee on a wooden board" points="0,86 470,64 470,526 0,526" fill="url(#brew-photo)"/>
      <polygon class="title-panel" points="420,70 920,8 920,526 440,526" fill="var(--leaf)"/>
      <path role="img" aria-label="Photo of roasted coffee beans" d="M0,470 C80,440 160,455 240,430 C330,410 420,440 500,420 C620,395 760,410 920,380 L920,526 L0,526 Z" fill="url(#bean-photo)"/>

      <g class="brand-badge">
        <circle cx="114" cy="104" r="80" fill="var(--cream)" stroke="var(--roast)" stroke-width="5"/>
        <text class="brand-name" x="114" y="111" text-anchor="middle">Pebble Kettle</text>
      </g>

      <text class="headline headline--light" x="560" y="132">Pebble</text>
      <text class="headline headline--roast" x="660" y="197">Kettle</text>
      <text class="headline headline--light" x="560" y="262">Loyalty</text>
      <text class="headline headline--roast" x="660" y="327">Card</text>

      <g class="contact-list">
        <rect x="500" y="399" width="13" height="13" rx="2" fill="var(--cream)"/>
        <text class="contact" x="522" y="412">FB: @pebblekettlemossford</text>
        <circle cx="506.5" cy="429" r="6.5" fill="none" stroke="var(--cream)" stroke-width="2"/>
        <text class="contact" x="522" y="436">Insta: Pebblekettle</text>
        <rect x="500" y="448" width="14" height="10" fill="none" stroke="var(--cream)" stroke-width="1.6"/>
        <polyline points="500,448 507,454 514,448" fill="none" stroke="var(--cream)" stroke-width="1.6"/>
        <text class="contact" x="522" y="460">Email: mossford@pebblekettle.example</text>
        <path d="M507,470 a5,5 0 0 1 5,5 c0,4 -5,9 -5,9 c0,0 -5,-5 -5,-9 a5,5 0 0 1 5,-5 z" fill="var(--cream)"/>
        <text class="contact" x="522" y="484">Address: No.4 Quill Row, ZX40 9KT</text>
        <path d="M502,494 l4,-1 2,4 -2,2 c1,2 3,4 5,5 l2,-2 4,2 -1,4 c-7,0 -14,-7 -14,-14 z" fill="var(--cream)"/>
        <text class="contact" x="522" y="507">Phone: 01999 462057</text>
      </g>
    </svg>
  </section>

  <!-- Back -->
  <section class="card card--back">
    <svg width="920" height="526" viewBox="0 0 920 526">
      <defs>
        <g id="cup">
          <path d="M-26,2 h46 c0,16 -10,26 -23,26 c-13,0 -23,-10 -23,-26 z"/>
          <path d="M20,7 c10,0 10,12 -2,13" fill="none" stroke-width="4"/>
          <ellipse cx="-3" cy="30" rx="36" ry="6"/>
          <path d="M-12,-22 c-6,6 6,10 0,18 M0,-26 c-6,6 6,10 0,20" fill="none" stroke-width="3"/>
        </g>
      </defs>
      <rect width="920" height="526" fill="var(--ink)"/>
      <rect class="stamp-field" width="920" height="363" fill="var(--leaf)"/>

      <g class="stamp-tiles">
        <rect x="42" y="37" width="112" height="115" fill="var(--cream)"/>
        <use href="#cup" x="98" y="90" fill="var(--leaf)" stroke="var(--leaf)"/>
        <circle cx="95" cy="100" r="10" fill="var(--cream)"/><text class="stamp-number" x="95" y="105" text-anchor="middle" fill="var(--leaf)">1</text>

        <rect x="178" y="37" width="112" height="115" fill="var(--roast)"/>
        <use href="#cup" x="234" y="90" fill="var(--cream)" stroke="var(--cream)"/>
        <circle cx="231" cy="100" r="10" fill="var(--roast)"/><text class="stamp-number" x="231" y="105" text-anchor="middle" fill="var(--cream)">2</text>

        <rect x="315" y="37" width="112" height="115" fill="var(--cream)"/>
        <use href="#cup" x="371" y="90" fill="var(--leaf)" stroke="var(--leaf)"/>
        <circle cx="368" cy="100" r="10" fill="var(--cream)"/><text class="stamp-number" x="368" y="105" text-anchor="middle" fill="var(--leaf)">3</text>

        <rect x="452" y="37" width="112" height="115" fill="var(--roast)"/>
        <use href="#cup" x="508" y="90" fill="var(--cream)" stroke="var(--cream)"/>
        <circle cx="505" cy="100" r="10" fill="var(--roast)"/><text class="stamp-number" x="505" y="105" text-anchor="middle" fill="var(--cream)">4</text>

        <rect x="42" y="173" width="112" height="115" fill="var(--cream)"/>
        <use href="#cup" x="98" y="226" fill="var(--leaf)" stroke="var(--leaf)"/>
        <circle cx="95" cy="236" r="10" fill="var(--cream)"/><text class="stamp-number" x="95" y="241" text-anchor="middle" fill="var(--leaf)">5</text>

        <rect x="178" y="173" width="112" height="115" fill="var(--roast)"/>
        <use href="#cup" x="234" y="226" fill="var(--cream)" stroke="var(--cream)"/>
        <circle cx="231" cy="236" r="10" fill="var(--roast)"/><text class="stamp-number" x="231" y="241" text-anchor="middle" fill="var(--cream)">6</text>

        <rect x="315" y="173" width="112" height="115" fill="var(--cream)"/>
        <use href="#cup" x="371" y="226" fill="var(--leaf)" stroke="var(--leaf)"/>
        <circle cx="368" cy="236" r="10" fill="var(--cream)"/><text class="stamp-number" x="368" y="241" text-anchor="middle" fill="var(--leaf)">7</text>

        <rect x="452" y="173" width="112" height="115" fill="var(--roast)"/>
        <use href="#cup" x="508" y="226" fill="var(--cream)" stroke="var(--cream)"/>
        <circle cx="505" cy="236" r="10" fill="var(--roast)"/><text class="stamp-number" x="505" y="241" text-anchor="middle" fill="var(--cream)">8</text>

        <rect x="587" y="173" width="112" height="115" fill="var(--cream)"/>
        <text class="free-label" x="643" y="226" text-anchor="middle">FREE</text>
        <text class="free-label" x="643" y="256" text-anchor="middle">COFFEE</text>
      </g>

      <g class="brand-badge">
        <circle cx="125" cy="408" r="75" fill="var(--cream)" stroke="var(--roast)" stroke-width="5"/>
        <text class="brand-name" x="125" y="415" text-anchor="middle">Pebble Kettle</text>
      </g>

      <text class="offer-title" x="882" y="414" text-anchor="end">LOYALTY CARD</text>
      <text class="offer-line" x="882" y="448" text-anchor="end">buys 8 coffees and</text>
      <text class="offer-line" x="882" y="480" text-anchor="end">gets the ninth free</text>
    </svg>
  </section>

</main>
</body>
</html>
```